Lanternfield Disability - Social Security Disability Attorneys

Our company is expanding to attract clients nationwide for our social security disability practice. We have a logo, but I am looking for a creative and elegant letterhead that projects an image of being technologically advanced but still professional enough for the legal field. I am looking for the "wow factor" combined with this is still professional enough for a law practice.

Requesting letterhead and business card design
Updates

Had to update and change the logo. The previous logo had a typo. Please send updates with the new logo for consideration. The letterhead and business cards should be professional enough to be used for a law firm. Thanks.

Industry/Entity Type

Law Practice, Law Firm, Healthcare Industry, Government

Colors

Designer to choose colors to be used in the design.

Requirements
Nice to have
• **Please create a vertical design for the business card**

```html
<!DOCTYPE html>
<html lang="en">
<head>
<meta charset="utf-8">
<title>Lanternfield Disability — Letterhead</title>
<link rel="stylesheet" href="https://fonts.googleapis.com/css2?family=Montserrat:wght@300;400;500&family=Roboto:wght@400;500&display=swap">
<style>
  :root {
    --backdrop: #d2d2d2;
    --paper: #efefef;
    --navy: #364a8a;
    --brand-blue: #3d56a0;
    --orange: #e87722;
    --peach: #e89c66;
    --ink: #2b2b2b;
    --body-ink: #555555;
    --rule-dark: #3a3a3a;
    --rule-blue: #2a9fd6;
    --rule-red: #e0394a;
    --signature: #bfe0f2;
  }
  * { margin: 0; padding: 0; box-sizing: border-box; }
  html, body { width: 1200px; height: 900px; overflow: hidden; }
  body {
    background: var(--backdrop);
    font-family: "Montserrat", sans-serif;
    position: relative;
  }
  .letterhead {
    position: absolute;
    top: 50px;
    width: 566px;
    height: 800px;
    background: var(--paper);
    overflow: hidden;
  }
  .letterhead--arc { left: 22px; }
  .letterhead--ribbon { left: 612px; }

  .header-art {
    position: absolute; left: 0; right: 0;
  }
  .letterhead--arc .header-art {
    top: 92px; height: 95px;
    background: linear-gradient(100deg, #5a7bbd 0%, #e87722 30%, #e89c66 60%, #efcfb4 100%);
    opacity: 0.85;
  }
  .letterhead--ribbon .header-art {
    top: 130px; height: 150px;
    background: linear-gradient(100deg, #364a8a 0%, #8a6a9a 35%, #e87722 70%, #c9651c 100%);
    opacity: 0.8;
  }

  .brand {
    position: absolute; left: 0; right: 0;
    display: flex; justify-content: center; align-items: center; gap: 7px;
  }
  .brand__dot {
    width: 8px; height: 8px; border-radius: 50%;
    background: var(--orange);
  }
  .brand__name {
    font-family: "Montserrat", sans-serif;
    font-weight: 500;
    text-transform: uppercase;
    letter-spacing: 1.2px;
    color: var(--brand-blue);
  }
  .letterhead--arc .brand { top: 56px; }
  .letterhead--arc .brand__name { font-size: 13px; }
  .letterhead--ribbon .brand { top: 89px; }
  .letterhead--ribbon .brand__name { font-size: 17px; }

  .sender {
    position: absolute; left: 0; right: 0;
    text-align: center;
  }
  .sender__name { font-size: 12.5px; font-weight: 500; color: var(--ink); }
  .sender__role { font-size: 8.5px; font-weight: 400; color: var(--body-ink); margin-top: 3px; }
  .sender__contact { margin-top: 18px; font-size: 8.2px; font-weight: 300; color: var(--ink); line-height: 16px; }
  .letterhead--arc .sender { top: 206px; }
  .letterhead--ribbon .sender { top: 292px; }

  .letter-body {
    position: absolute; left: 66px; width: 450px;
    font-size: 7.9px; font-weight: 400; line-height: 16px;
    color: var(--body-ink); text-align: justify;
  }
  .letter-body p + p { margin-top: 16px; }
  .letterhead--arc .letter-body { top: 358px; }
  .letterhead--ribbon .letter-body { top: 418px; }

  .footer-contact {
    position: absolute; left: 66px; width: 254px;
    border-top: 1.5px solid var(--rule-dark);
    border-bottom: 1.5px solid var(--rule-blue);
    padding: 6px 0 6px;
    display: flex;
    font-family: "Roboto", sans-serif;
    font-size: 9.5px; line-height: 12.5px;
  }
  .letterhead--arc .footer-contact { top: 676px; }
  .letterhead--ribbon .footer-contact { top: 703px; border-bottom-color: var(--rule-red); }
  .footer-contact__item { width: 135px; color: #4a4a4a; }
  .footer-contact__item strong { display: block; font-weight: 500; color: var(--ink); }

  .signoff { position: absolute; left: 402px; }
  .letterhead--arc .signoff { top: 667px; }
  .letterhead--ribbon .signoff { top: 686px; }
  .signoff__signature {
    width: 72px; height: 28px; border-radius: 3px;
    background: var(--signature);
  }
  .signoff__name { font-family: "Roboto", sans-serif; font-weight: 500; font-size: 12px; color: var(--ink); margin-top: 4px; }
  .signoff__role { font-family: "Roboto", sans-serif; font-size: 8.5px; color: #4a4a4a; margin-top: 1px; }
</style>
</head>
<body>

<section class="letterhead letterhead--arc">
  <div class="header-art" role="img" aria-label="Decorative sweeping orange and blue wave artwork"></div>

  <div class="brand">
    <span class="brand__dot"></span>
    <span class="brand__name">Lanternfield Disability</span>
  </div>

  <div class="sender">
    <div class="sender__name">Evan Holloway</div>
    <div class="sender__role">Creative Director</div>
    <div class="sender__contact">
      Your location address here, usa-123<br>
      email@youremail.com, www.yourweb.com<br>
      +1-222-333-444
    </div>
  </div>

  <div class="letter-body">
    <p>This is a sample letter that has been placed to demonstrate the typing format on the (Your Company) letterhead design. When positioned properly, it will serve to work in harmony with all of the core an other elements on the letterhead This letterhead design is meant to project an image of professionalism and reliability. By using simple alignments we have created a very spacious feeling uggests strength and the image of professionalism and reliability. By using simple alignments we have.</p>
    <p>Been placed to demonstrate the typing format on the (Your Company) letterhead design. When positioned properly, it will serve to work in harmony with all of the core an other elements on the letterhead This letterhead design is meant to project an image of professionalism and reliability. By using simple alignments we have created.</p>
    <p>Placed to demonstrate the typing format on the (Your Company) letterhead design. When positioned properly, it will serve to work in harmony with all of the core an other elements on the letterhead This letterhead design is meant to project an image.</p>
  </div>

  <div class="footer-contact">
    <div class="footer-contact__item"><strong>Our Street Adress 1</strong>Street 75400 Ashvale</div>
    <div class="footer-contact__item"><strong>Our Phone</strong>+1 555 0100 2233</div>
  </div>

  <div class="signoff">
    <div class="signoff__signature" role="img" aria-label="Handwritten signature"></div>
    <div class="signoff__name">Jonah Pell</div>
    <div class="signoff__role">Director</div>
  </div>
</section>

<section class="letterhead letterhead--ribbon">
  <div class="header-art" role="img" aria-label="Decorative crossing blue and orange ribbon artwork"></div>

  <div class="brand">
    <span class="brand__dot"></span>
    <span class="brand__name">Lanternfield Disability</span>
  </div>

  <div class="sender">
    <div class="sender__name">Evan Holloway</div>
    <div class="sender__role">Creative Director</div>
    <div class="sender__contact">
      Your location address here, usa-123<br>
      email@youremail.com, www.yourweb.com<br>
      +1-222-333-444
    </div>
  </div>

  <div class="letter-body">
    <p>This is a sample letter that has been placed to demonstrate the typing format on the (Your Company) letterhead design. When positioned properly, it will serve to work in harmony with all of the core an other elements on the letterhead This letterhead design is meant to project an image of professionalism and reliability. By using simple alignments we have created a very spacious feeling uggests strength and the image of professionalism and reliability. By using simple alignments we have.</p>
    <p>Been placed to demonstrate the typing format on the (Your Company) letterhead design. When positioned properly, it will serve to work in harmony with all of the core an other elements on the letterhead This letterhead design is meant to project an image of professionalism and reliability. By using simple alignments we have created.</p>
    <p>Placed to demonstrate the typing format on the (Your Company) letterhead design. When positioned properly, it will serve to work in harmony with all of the core an other elements on the letterhead This letterhead design is meant to project an image.</p>
  </div>

  <div class="footer-contact">
    <div class="footer-contact__item"><strong>Our Street Adress 1</strong>Street 75400 Ashvale</div>
    <div class="footer-contact__item"><strong>Our Phone</strong>+1 555 0100 2233</div>
  </div>

  <div class="signoff">
    <div class="signoff__signature" role="img" aria-label="Handwritten signature"></div>
    <div class="signoff__name">Jonah Pell</div>
    <div class="signoff__role">Director</div>
  </div>
</section>

</body>
</html>
```